business card for author of crime novel

I am an author with a new book. I need a business card with the book's cover on one side (already uploaded), and contact details on the other.

Tom Velasquin
Author

telephone: 917-555-0162
website: www.tomvelasquin.example
facebook: friendpage.example/tvelasquin
twitter: chirpline.example/tvelasquin
email: tvelasquin@mailbox.example

Target Market(s)

Readers of mystery books

Industry/Entity Type

Business

Contact Information for Business Card

Tom Velasquin
Author

telephone: 917-555-0162

Font styles to use
Serif
Sans Serif

Requirements
Must have
• Book cover on one side. My contact info on the other, with the name of the book repeated if that makes sense. Clean design.
Should not have
• Overly ornate, too formal, too distracting

```html
<!DOCTYPE html>
<html lang="en">
<head>
<meta charset="utf-8">
<title>Dead Static Blues – Tom Velasquin, Author</title>
<link rel="stylesheet" href="https://fonts.googleapis.com/css2?family=Old+Standard+TT:wght@700&family=Cinzel:wght@400&family=IM+Fell+English&family=Roboto:wght@400;700&display=swap">
<style>
  :root {
    --page: #e9e9e7;
    --amber: #e1a12a;
    --slate: #353a45;
    --rule: #d39a2c;
    --ink: #111111;
    --white: #ffffff;
    --cover-name: #e8d64c;
    --plaque-light: #efdcb4;
    --plaque-dark: #cfae78;
    --contact-text: #f1f1f1;
  }
  * { box-sizing: border-box; margin: 0; padding: 0; }
  html, body { width: 1200px; height: 863px; overflow: hidden; }
  body { background: var(--page); position: relative; font-family: "Roboto", Arial, sans-serif; }

  .card {
    position: absolute;
    top: 143px;
    width: 330px;
    height: 578px;
    box-shadow: 0 6px 18px rgba(0,0,0,0.18);
    overflow: hidden;
  }

  /* Front: book cover */
  .card--cover { left: 240px; background: var(--amber); }
  .cover__title {
    position: absolute; top: 30px; left: 0; width: 100%;
    text-align: center;
    font-family: "Old Standard TT", Georgia, serif;
    font-weight: 700; font-size: 25px; letter-spacing: 0.5px;
    color: var(--ink); text-transform: uppercase;
  }
  .cover__art {
    position: absolute; top: 74px; left: 26px; width: 278px; height: 440px;
    background: linear-gradient(160deg, #8fa7b3 0%, #5f7886 40%, #3c4e5a 75%, #25313a 100%);
  }
  .cover__author {
    position: absolute; right: 38px; top: 410px;
    text-align: right;
    font-family: "Cinzel", Georgia, serif;
    font-size: 22px; line-height: 1.05;
    color: var(--cover-name); text-transform: uppercase;
  }
  .cover__series {
    position: absolute; left: 42px; top: 486px; width: 246px; height: 40px;
    border-radius: 4px;
    background: linear-gradient(180deg, var(--plaque-light), var(--plaque-dark));
    display: flex; align-items: center; justify-content: center;
    font-family: "IM Fell English", Georgia, serif;
    font-size: 18px; color: var(--ink);
  }

  /* Back: contact details */
  .card--contact { left: 630px; background: var(--slate); }
  .contact__band { height: 14px; background: var(--amber); }
  .contact__head { background: var(--white); height: 196px; text-align: center; }
  .contact__title {
    padding-top: 38px;
    font-family: "Old Standard TT", Georgia, serif;
    font-weight: 700; font-size: 26px; letter-spacing: 0.5px;
    color: var(--amber); text-transform: uppercase;
  }
  .contact__name { margin-top: 28px; font-weight: 700; font-size: 24px; color: var(--ink); }
  .contact__role { font-size: 20px; color: var(--ink); padding-left: 40px; }

  .contact__list { list-style: none; padding: 14px 20px 0; }
  .contact__item {
    position: relative;
    height: 62px;
    display: flex; align-items: center; justify-content: center; gap: 10px;
    font-size: 16px; color: var(--contact-text);
    white-space: nowrap;
  }
  .contact__item::before {
    content: ""; position: absolute; left: 6px; right: 6px; top: -1px;
    border-top: 2px solid var(--rule);
  }
  .contact__item:last-child::after {
    content: ""; position: absolute; left: 6px; right: 6px; bottom: -1px;
    border-top: 2px solid var(--rule);
  }
  .dot {
    position: absolute; width: 10px; height: 10px; border-radius: 50%;
    background: var(--amber); top: -5px;
  }
  .dot--left { left: 0; }
  .dot--right { right: 0; }
  .contact__item:last-child .dot--bottom { top: auto; bottom: -5px; }
  .contact__icon { width: 16px; height: 16px; flex: none; fill: var(--amber); }
  .contact__badge { width: 12px; height: 12px; flex: none; background: var(--amber); border-radius: 2px; }
</style>
</head>
<body>

<section class="card card--cover" aria-label="Book cover">
  <h1 class="cover__title">Dead Static Blues</h1>
  <div class="cover__art" role="img" aria-label="Blue-toned photograph of an old city tenement building with fire escapes"></div>
  <p class="cover__author">Tom<br>Velasquin</p>
  <p class="cover__series">A Marlow Keane Mystery</p>
</section>

<section class="card card--contact" aria-label="Contact details">
  <div class="contact__band"></div>
  <header class="contact__head">
    <h2 class="contact__title">Dead Static Blues</h2>
    <p class="contact__name">Tom Velasquin</p>
    <p class="contact__role">Author</p>
  </header>
  <ul class="contact__list">
    <li class="contact__item">
      <span class="dot dot--left"></span><span class="dot dot--right"></span>
      <svg class="contact__icon" viewBox="0 0 24 24" aria-hidden="true"><path d="M6.6 10.8a15.2 15.2 0 0 0 6.6 6.6l2.2-2.2a1 1 0 0 1 1-.25 11.4 11.4 0 0 0 3.6.57 1 1 0 0 1 1 1V20a1 1 0 0 1-1 1A17 17 0 0 1 3 4a1 1 0 0 1 1-1h3.5a1 1 0 0 1 1 1c0 1.25.2 2.45.57 3.6a1 1 0 0 1-.25 1z"/></svg>
      <span>917-555-0162</span>
    </li>
    <li class="contact__item">
      <span class="dot dot--left"></span><span class="dot dot--right"></span>
      <svg class="contact__icon" viewBox="0 0 24 24" aria-hidden="true"><path d="M2 5h20v14H2z M2 5l10 8 10-8" fill="none" stroke="#e1a12a" stroke-width="2"/></svg>
      <span>tvelasquin@mailbox.example</span>
    </li>
    <li class="contact__item">
      <span class="dot dot--left"></span><span class="dot dot--right"></span>
      <span class="contact__badge"></span>
      <span>friendpage.example/tvelasquin</span>
    </li>
    <li class="contact__item">
      <span class="dot dot--left"></span><span class="dot dot--right"></span>
      <span class="contact__badge"></span>
      <span>chirpline.example/tvelasquin</span>
    </li>
    <li class="contact__item">
      <span class="dot dot--left"></span><span class="dot dot--right"></span>
      <span class="dot dot--left dot--bottom"></span><span class="dot dot--right dot--bottom"></span>
      <svg class="contact__icon" viewBox="0 0 24 24" aria-hidden="true"><path d="M2 4h20v16H2z M2 8h20" fill="none" stroke="#e1a12a" stroke-width="2"/></svg>
      <span>www.tomvelasquin.example</span>
    </li>
  </ul>
</section>

</body>
</html>
```